Fahrzeugbeschriftung für Elektrotechnik-Betrieb
Zielgruppe
Unser Kunde ist ein Elektrotechnik Betrieb mit Sitz in Hamburg. Zu uns kamen sie mit dem Wunsch nach einer Webseite für Ihren Imageaufbau. Der Meisterbetrieb beschäftigt sich mit Neu- und Altbausanierung, Schiffselektrik (USP), Wartung, Reparatur, Installation, E-Check...
Zielgruppe ist vorwiegend das Gewerbe.
Die Domain der entstehenden Webseite: kvr-stromtechnik.de
Adresse: Am Lindenbruch 12, 22147 Hamburg
Telefonnummer: 04031874520
Entwurf der Webseite: https://vorlagenhof.de/kvr.jpg
Bitte das Design beachten, sonst gerne kreativ und auffällig!
Aufgabenstellung
Der Kunde hätte das Autodesign gerne schlicht und modern. Im Fokus stehen die Leistungen. Ebenfalls sollen Logo (befindet sich im Anhang), Telefonnummer und Webseite klar zu sehen sein.
Nähere Vorgaben:
-Vorne: nur das Logo
-Seiten: Leistungen, Logo, Telefonnummer, Webseite
-Hinten: Logo ; Telefonnummer und Webseite
Design muss auf folgendes Modell passen: Varelo Kastro, weiß
Vorschläge/Beispiele sind im Anhang!!!

```html
<!DOCTYPE html>
<html lang="de">
<head>
<meta charset="utf-8">
<title>KVR Stromtechnik – Fahrzeugbeschriftung</title>
<link rel="stylesheet" href="https://fonts.googleapis.com/css2?family=Montserrat:wght@500&family=Nunito:wght@600;800&display=swap">
<style>
  :root {
    --stage: #545456;
    --stage-light: #5e5e60;
    --panel: #f4f4f5;
    --panel-shade: #dcdcde;
    --ink: #2c2b2c;
    --band: #333234;
    --white: #ffffff;
  }
  * { margin: 0; padding: 0; box-sizing: border-box; }
  html, body { width: 932px; height: 1200px; overflow: hidden; }
  body {
    background: radial-gradient(ellipse at 50% 45%, var(--stage-light), var(--stage) 70%);
    position: relative;
    font-family: "Nunito", sans-serif;
    color: var(--ink);
  }
  .panel { position: absolute; border-radius: 22px; overflow: hidden;
    background: linear-gradient(180deg, var(--white), var(--panel) 60%, var(--panel-shade)); }
  .side-view { left: 140px; top: 297px; width: 668px; height: 259px; border-radius: 30px 60px 40px 30px; }
  .front-view { left: 129px; top: 629px; width: 357px; height: 267px; border-radius: 40px 40px 24px 24px; }
  .rear-view { left: 555px; top: 637px; width: 269px; height: 264px; border-radius: 30px 30px 18px 18px; }
  .base { position: absolute; left: 0; right: 0; bottom: 0; background: var(--band); }
  .abs { position: absolute; white-space: nowrap; }
  .wordmark { font-family: "Montserrat", sans-serif; font-weight: 500; color: var(--ink); letter-spacing: 2px; line-height: 1; }
  .company { font-family: "Montserrat", sans-serif; font-weight: 500; color: var(--ink); line-height: 1; }
  .service { font-weight: 800; font-size: 13.5px; line-height: 1; display: flex; align-items: center; gap: 7px; }
  .service svg { width: 15px; height: 15px; flex: none; }
  .service-band { position: absolute; left: 157px; top: 165px; width: 374px; height: 25px; background: var(--band);
    color: var(--white); display: flex; align-items: center; padding-left: 30px; gap: 7px; }
  .service-band svg { width: 15px; height: 15px; }
  .ghost-mark { font-family: "Montserrat", sans-serif; font-weight: 500; font-size: 120px; color: rgba(0,0,0,.05); letter-spacing: 6px; }
  .contact { font-size: 7.5px; font-weight: 600; line-height: 1.15; }
  .rear-line { font-weight: 800; color: var(--ink); }
</style>
</head>
<body>

<section class="panel side-view" aria-label="Seitenansicht">
  <div class="base" style="height:22px"></div>
  <div class="abs ghost-mark" style="left:150px; top:112px">KVR</div>
  <div class="abs wordmark" style="left:68px; top:32px; font-size:36px">KVR</div>
  <div class="abs company" style="left:167px; top:43px; font-size:13px">Stromtechnik GmbH</div>

  <div class="abs service" style="left:187px; top:115px">
    <svg viewBox="0 0 16 16"><circle cx="8" cy="8" r="8" fill="var(--ink)"/><path d="M3.5 9h9l-1.5 2.5h-6z M6 6h4v3H6z" fill="#fff"/></svg>
    Schiffselektrik
  </div>
  <div class="abs service" style="left:50px; top:136px">
    <svg viewBox="0 0 16 16"><circle cx="8" cy="8" r="8" fill="var(--ink)"/><path d="M8 3.8l4 3.6h-1.2v4.2H9V9.3H7v2.3H5.2V7.4H4z" fill="#fff"/></svg>
    Neu-und Altbausanierung
  </div>
  <div class="abs service" style="left:265px; top:136px">
    <svg viewBox="0 0 16 16"><circle cx="8" cy="8" r="8" fill="var(--ink)"/><path d="M4 9.5l8-4M4.5 11l7-3.5" stroke="#fff" stroke-width="1.6" fill="none"/></svg>
    E-Check
  </div>
  <div class="service-band service">
    <svg viewBox="0 0 16 16"><circle cx="8" cy="8" r="8" fill="#fff"/><path d="M9 3L5 9h3l-1 4 4-6H8z" fill="var(--band)"/></svg>
    Wartung, Reparatur und Installation
  </div>

  <div class="abs contact" style="left:385px; top:126px">
    Am Lindenbruch 12<br>22147 Hamburg<br>Tel. +49 (0) 40 318 745 20<br>www.kvr-stromtechnik.de
  </div>
</section>

<section class="panel front-view" aria-label="Frontansicht">
  <div class="base" style="height:92px"></div>
  <div class="abs wordmark" style="left:184px; top:86px; font-size:20px">KVR</div>
  <div class="abs company" style="left:158px; top:110px; font-size:5px">KVR Stromtechnik GmbH</div>
</section>

<section class="panel rear-view" aria-label="Heckansicht">
  <div class="base" style="height:32px"></div>
  <div class="abs wordmark" style="left:100px; top:20px; font-size:34px">KVR</div>
  <div class="abs company" style="left:92px; top:61px; font-size:7px">Stromtechnik GmbH</div>
  <div class="abs rear-line" style="left:62px; top:91px; font-size:12px">Tel. +49 (0) 40 318 745 20</div>
  <div class="abs rear-line" style="left:63px; top:187px; font-size:11px">www.kvr-stromtechnik.de</div>
</section>

</body>
</html>
```